Computer Training in the Education sector - Letterhead

We need a new letter head to be designed for the company. We provide computer training fro the Education Sector, both primary and private tertiary providers. The colours will need to tie in with the website www.lanternpathlearning.co.nz.
The company name is Lantern Path Co with the tag line of Computer Training for Educators.
The footer will need to have the following detail...
0508 KEY MENTOR
027 813 459
www.lanternpathlearning.co.nz / lessons@lanternpathlearning.co.nz
Updates

Thanks for the designs so far.

Some have watermarks in the background. Please don't worry about using watermarks as I will not be using a watermark in in a final design.
Regards,
Morris

Thank you for all the designs and the effort. There was some great concepts that came through.

Cheers
Morris

Industry/Entity Type

Computer

```html
<!DOCTYPE html>
<html lang="en">
<head>
<meta charset="utf-8">
<title>Lantern Path Co – Letterhead</title>
<link href="https://fonts.googleapis.com/css2?family=Carlito:wght@400;700&family=Tinos:wght@400;700&display=swap" rel="stylesheet">
<style>
  :root {
    --paper: #ffffff;
    --ink: #1a1a1a;
    --brand-green: #7cb342;
    --brand-blue: #2b77c0;
    --bar-green: #8bbf4a;
    --bar-blue: #3f7fc4;
    --bar-orange: #f0913a;
  }
  * { margin: 0; padding: 0; box-sizing: border-box; }
  html, body { width: 927px; height: 1200px; overflow: hidden; background: var(--paper); }
  .letterhead { position: relative; width: 927px; height: 1200px; background: var(--paper); color: var(--ink); }

  .brand { position: absolute; left: 88px; top: 46px; display: flex; align-items: center; gap: 10px; }
  .brand-mark { width: 22px; height: 22px; border-radius: 50%; background: var(--brand-green); }
  .brand-name { font-family: "Carlito", "Calibri", sans-serif; font-weight: 700; font-size: 30px; color: var(--brand-green); line-height: 1; }
  .tagline { position: absolute; left: 122px; top: 112px; font-family: "Carlito", "Calibri", sans-serif; font-size: 17px; color: var(--brand-blue); }

  .letter { position: absolute; left: 109px; top: 160px; width: 709px; font-family: "Tinos", "Times New Roman", serif; font-size: 16px; line-height: 20.5px; }
  .salutation { margin-bottom: 18px; }
  .letter-title { text-align: center; font-weight: 700; text-decoration: underline; margin-bottom: 16px; }
  .letter p.body { text-align: justify; margin-bottom: 20px; }
  .letter p.body.lead { text-align: left; margin-bottom: 26px; }
  .closing { margin-top: 44px; }
  .signature-line { width: 138px; border-bottom: 1px solid var(--ink); margin-top: 32px; }
  .signatory { margin-top: 2px; }

  .contact { position: absolute; left: 330px; top: 1090px; display: grid; grid-template-columns: auto auto; column-gap: 3px; row-gap: 1px; font-family: "Carlito", "Calibri", sans-serif; font-size: 12.5px; line-height: 18px; color: var(--ink); }
  .contact dt { text-align: right; }
  .contact dd { text-align: left; }

  .footer-bands { position: absolute; left: 30px; top: 1165px; width: 864px; height: 11px; display: flex; gap: 3px; }
  .band { height: 100%; }
  .band-green { width: 304px; background: var(--bar-green); }
  .band-blue { width: 304px; background: var(--bar-blue); }
  .band-orange { flex: 1; background: var(--bar-orange); }
</style>
</head>
<body>
<div class="letterhead">
  <header>
    <div class="brand">
      <span class="brand-mark"></span>
      <span class="brand-name">Lantern Path Co</span>
    </div>
    <div class="tagline">Computer Training for Educators</div>
  </header>

  <main class="letter">
    <p class="salutation">Dear Sir/Madam:</p>
    <h1 class="letter-title" style="font-size:16px;">SAMPLE LETTER</h1>
    <p class="body lead">I would like to propose my candidacy for any available position within your organization. I posses six (6) subjects (General and Technical Level) at the Regional Secondary Education Certificate (RSEC) which I hope would allow for your consideration.</p>
    <p class="body">I am enthusiastically applying for an available position because I firmly believe that a combination of my natural ability, commitment, dedication, an interest in the telecommunications industry, intellectual ability, ability to handle pressure, technical expertise and work experience all make me an ideal candidate for your organization.</p>
    <p class="body">I have an ability to grow with a job, handle responsibility and build positive relationships with work colleagues at all levels.</p>
    <p class="body">I will be willing to attend any forum for interview if deemed necessary.</p>
    <p class="body">Please refer to the accompanying Curriculum Vitae for more detailed information regarding my abilities and competency.</p>
    <p class="closing">Yours Truly,</p>
    <div class="signature-line"></div>
    <p class="signatory">SAMPLE LETTER</p>
  </main>

  <footer>
    <dl class="contact">
      <dt>Toll Free Phone:</dt><dd>0508 KEY MENTOR</dd>
      <dt>Mobile:</dt><dd>027 813 459</dd>
      <dt>Website:</dt><dd>www.lanternpathlearning.co.nz</dd>
      <dt>Email:</dt><dd>lessons@lanternpathlearning.co.nz</dd>
    </dl>
    <div class="footer-bands">
      <span class="band band-green"></span>
      <span class="band band-blue"></span>
      <span class="band band-orange"></span>
    </div>
  </footer>
</div>
</body>
</html>
```